Ridgeway Claims Group Business card

We need to get business card Design for our Company we are Public Adjusters in Chicago Illinois - i like to see good combination and elements from my Company Logo. as well To be an two side design

Target Market(s)

Home /Business owner Property Managers

Industry/Entity Type

Business

Contact Information for Business Card

to show the Element of our logo i will Like 3D

Font styles to use
Sans Serif

Requirements
Must have
• Logo and Element of the Logo in 3D
Nice to have
• Logo That we Provide 3D Same Colors or open for suggestions
Should not have
• unleare view -

```html
<!DOCTYPE html>
<html lang="en">
<head>
<meta charset="utf-8">
<title>Ridgeway Claims Group – Business Card</title>
<link href="https://fonts.googleapis.com/css2?family=Arimo:wght@400;700&display=swap" rel="stylesheet">
<style>
  :root {
    --page-bg: #3a3a3a;
    --card-white: #ffffff;
    --navy: #0c1a6e;
    --royal: #1230b8;
    --brand-orange: #e2573a;
    --text-grey: #4a4a4a;
    --icon-blue: #1a2aa8;
    --link-blue: #1b2f9e;
  }
  * { margin: 0; padding: 0; box-sizing: border-box; }
  html, body {
    width: 1105px; height: 1200px; overflow: hidden;
    background: var(--page-bg);
    font-family: "Arimo", Arial, sans-serif;
  }
  .card {
    position: absolute; left: 196px; width: 719px; height: 410px;
    overflow: hidden;
  }
  .card--front { top: 146px; background: var(--card-white); }
  .card--back { top: 602px; background: var(--brand-orange); }

  .front-swoosh { position: absolute; inset: 0; width: 719px; height: 410px; }

  .holder { position: absolute; left: 37px; top: 24px; color: var(--card-white); }
  .holder__name { font-weight: 700; font-size: 24px; letter-spacing: 0.5px; }
  .holder__role { font-size: 19px; margin-top: 4px; }

  .contact-list { position: absolute; left: 38px; top: 268px; list-style: none; }
  .contact-list li {
    display: flex; align-items: center; height: 27.5px;
    font-size: 18px; color: var(--text-grey);
  }
  .contact-list li:last-child { font-size: 17px; }
  .contact-list svg { width: 18px; height: 18px; margin-right: 9px; fill: var(--icon-blue); flex: none; }

  .brand-mark { position: absolute; right: 30px; top: 84px; width: 270px; text-align: center; }
  .brand-mark__dot {
    width: 104px; height: 104px; border-radius: 50%;
    background: var(--royal); margin: 0 auto 52px;
  }
  .brand-mark__name { font-weight: 700; font-size: 17px; color: var(--royal); white-space: nowrap; }

  .address {
    position: absolute; right: 32px; top: 300px; text-align: right;
    font-size: 18px; color: var(--text-grey); line-height: 25.5px;
  }
  .address__web { color: var(--link-blue); letter-spacing: 2.5px; font-size: 17px; }

  .back-mark { position: absolute; left: 0; right: 0; top: 78px; text-align: center; }
  .back-mark__dot {
    width: 160px; height: 160px; border-radius: 50%;
    background: var(--royal); margin: 0 auto 26px;
  }
  .back-mark__name { font-weight: 700; font-size: 26px; color: var(--card-white); white-space: nowrap; }
  .back-web {
    position: absolute; left: 0; right: 0; top: 347px; text-align: center;
    color: var(--card-white); font-size: 17px; letter-spacing: 3px;
  }
</style>
</head>
<body>

<section class="card card--front">
  <svg class="front-swoosh" viewBox="0 0 719 410" aria-hidden="true">
    <defs>
      <linearGradient id="navyBand" x1="0" y1="0" x2="1" y2="0">
        <stop offset="0" stop-color="#0a1560"/>
        <stop offset="0.55" stop-color="#1230b8"/>
        <stop offset="1" stop-color="#0c1a6e"/>
      </linearGradient>
    </defs>
    <path d="M0,0 H719 V42 C480,36 200,70 0,196 Z" fill="url(#navyBand)"/>
    <path d="M0,198 C200,80 440,46 660,44 C460,56 210,120 0,232 Z" fill="var(--brand-orange)"/>
  </svg>

  <div class="holder">
    <p class="holder__name">ALEX MORAN</p>
    <p class="holder__role">President</p>
  </div>

  <ul class="contact-list">
    <li><svg viewBox="0 0 20 20"><path d="M2 7c0-3 3-4 8-4s8 1 8 4v2h-4V7H6v2H2z M5 10h10l2 7H3z"/></svg>312 555 0148</li>
    <li><svg viewBox="0 0 20 20"><path d="M6 1h8a1 1 0 0 1 1 1v16a1 1 0 0 1-1 1H6a1 1 0 0 1-1-1V2a1 1 0 0 1 1-1zm1 2v12h6V3z"/></svg>312 555 0172</li>
    <li><svg viewBox="0 0 20 20"><path d="M5 2h10v5H5z M2 8h16v8h-3v3H5v-3H2z M7 13v4h6v-4z"/></svg>312 555 0190</li>
    <li><svg viewBox="0 0 20 20"><path d="M2 5h16v10H2z"/><path d="M3 6l7 5 7-5" fill="none" stroke="#fff" stroke-width="1.5"/></svg>alex@rcgoffice.com</li>
  </ul>

  <div class="brand-mark">
    <div class="brand-mark__dot"></div>
    <p class="brand-mark__name">Ridgeway Claims Group, Inc.</p>
  </div>

  <div class="address">
    <p>2170 Harbor Lane</p>
    <p>Maple Ridge, IL 60412</p>
    <p class="address__web">www.rcgoffice.com</p>
  </div>
</section>

<section class="card card--back">
  <div class="back-mark">
    <div class="back-mark__dot"></div>
    <p class="back-mark__name">Ridgeway Claims Group</p>
  </div>
  <p class="back-web">www.RidgewayClaims.com</p>
</section>

</body>
</html>
```